Business Cards for IT Consulting Company (Managed Service Provider)

I am looking to have some business cards printed and would like some designs. We are an IT Consulting company based in Vancouver BC. I would like a nice clean and modern look to the cards. I have uploaded all the versions of my logo so parts can be used as needed. Here is a snippit from our website homepage:

Kelbrook Systems Ltd. is an IT Solutions Partner located in Vancouver BC, Canada. We offer IT solutions and support to customers in the greater Vancouver Area. With expertise in Microsoft platforms, as well as Linux and Mac OSX and over 12 years experience in the IT industry, Kelbrook Systems is dedicated to offering our clients top quality service and products. We take pride in the solutions we offer our customers. The greatest compliment a client can give us is to recommend our services.

Kelbrook Systems Ltd. offers a wide range of IT services from onsite service to remote support and managed service solutions. This allows clients to choose the support path that best suits their company’s needs. Supporting many different sized companies from small to enterprise level over the past 12 years Kelbrook Systems has the experience and expertise needed to ensure things run smoothly. Allowing our clients to focus on doing business.

Revolutionizing the way IT services are delivered.

Kelbrook Systems is dedicated to providing our clients with IT solutions that work and grow with them for years to come. This philosophy helps save money in the long run instead of replacing equipment constantly. Far too often IT solutions are not well thought out and while possibly solving the problem at hand, require replacement due to growth or quality within a very short time frame. Kelbrook Systems takes pride in providing solutions that will last and be able to accommodate growth without the need for replacement.

Industry/Entity Type

Information Technology

Contact Information for Business Card

Kelbrook Systems Ltd.
(Employee Name)
Eml: (Employees Email Address)
Web: kelbrook.me
Ph: 604-555-0142

Font styles to use
Serif
Sans Serif

Requirements
Must have
• The Company logo and company colors.
Nice to have
• - Our tag line: "Revolutionizing IT Services" or "Revolutionizing the way IT services are delivered."
• - Also I really like the idea of nature and technology together blending which is sort of where my logo came from so integrating that somehow onto the business cards would be great.

```html
<!DOCTYPE html>
<html lang="en">
<head>
<meta charset="utf-8">
<title>Kelbrook Systems Ltd. – Business Cards</title>
<link rel="stylesheet" href="https://fonts.googleapis.com/css2?family=Open+Sans:wght@400;600;700&display=swap">
<style>
  :root {
    --backdrop: #cbcbcb;
    --paper: #ffffff;
    --brand-blue: #1aa0dc;
    --card-blue: #6fb4e1;
    --ink-grey: #4a4a4a;
    --ink-white: #ffffff;
  }
  * { box-sizing: border-box; margin: 0; padding: 0; }
  html, body {
    width: 1200px; height: 1200px; overflow: hidden;
    background: var(--backdrop);
    font-family: "Open Sans", Arial, sans-serif;
  }
  .card {
    position: absolute;
    left: 220px;
    width: 760px; height: 434px;
    box-shadow: 0 10px 28px rgba(0,0,0,0.18);
    overflow: hidden;
  }
  .card-front { top: 110px; background: var(--paper); }
  .card-back  { top: 650px; background: var(--card-blue); color: var(--ink-white); }

  .brand {
    position: absolute; left: 170px; top: 150px;
    display: flex; align-items: center; gap: 18px;
  }
  .brand-mark { width: 44px; height: 44px; background: var(--brand-blue); }
  .brand-name {
    font-size: 50px; font-weight: 700; color: var(--brand-blue);
    line-height: 1; letter-spacing: -0.5px;
  }
  .tagline {
    position: absolute; left: 170px; top: 300px;
    font-size: 16px; letter-spacing: 6px; color: var(--ink-grey);
  }

  .back-pattern {
    position: absolute; left: 0; top: 0;
    width: 390px; height: 100%;
    background: linear-gradient(135deg,
      rgba(26,160,220,0.75) 0%,
      rgba(26,160,220,0.45) 55%,
      rgba(26,160,220,0.10) 100%);
  }

  .contact-block {
    position: absolute; right: 56px; top: 70px;
    text-align: right;
  }
  .company-line { font-size: 25px; font-weight: 400; }
  .company-line strong { font-weight: 700; }
  .employee-name { font-size: 36px; font-weight: 700; margin-top: 6px; }
  .details { list-style: none; margin-top: 48px; font-size: 21px; line-height: 1.45; }
  .details li { display: flex; justify-content: flex-end; align-items: center; gap: 14px; }
  .details svg { width: 22px; height: 22px; flex: none; }
</style>
</head>
<body>
  <section class="card card-front" aria-label="Card front">
    <div class="brand">
      <span class="brand-mark"></span>
      <span class="brand-name">Kelbrook Systems</span>
    </div>
    <p class="tagline">Revolutionizing IT Services</p>
  </section>

  <section class="card card-back" aria-label="Card back">
    <div class="back-pattern" role="img" aria-label="Large decorative brand pattern in blue outlines"></div>
    <div class="contact-block">
      <p class="company-line"><strong>Kelbrook</strong> Systems Ltd.</p>
      <p class="employee-name">(Employee Name)</p>
      <ul class="details">
        <li>604-555-0142
          <svg viewBox="0 0 24 24" aria-hidden="true"><path fill="#fff" d="M3 9c0-3 4-5 9-5s9 2 9 5v2h-5V9c-1-.6-2.5-1-4-1s-3 .4-4 1v2H3zM6 13h12l2 7H4z"/></svg>
        </li>
        <li>kelbrook.me
          <svg viewBox="0 0 24 24" aria-hidden="true"><circle cx="12" cy="12" r="9" fill="none" stroke="#fff" stroke-width="2"/><ellipse cx="12" cy="12" rx="4" ry="9" fill="none" stroke="#fff" stroke-width="1.6"/><path d="M3 12h18" stroke="#fff" stroke-width="1.6"/></svg>
        </li>
        <li>(Employees Email Address)
          <svg viewBox="0 0 24 24" aria-hidden="true"><rect x="2" y="5" width="20" height="14" fill="#fff"/><path d="M2 5l10 8 10-8" fill="none" stroke="#6fb4e1" stroke-width="1.6"/></svg>
        </li>
      </ul>
    </div>
  </section>
</body>
</html>
```